Business Card Professional Clean - Ledgerpeak

Create a business card for my company that deals with Cryptocurrencies. I have a few designs ideas that I'd like to be implemented. Thanks! I will include the logo files, and a link to the design styles that I like.

Target Market(s)

Professionals

Industry/Entity Type

Consulting

Contact Information for Business Card

Name: Mark Dunn
Title: CEO/Technical Director
Phone: (587)430-9158
E-mail: mdunn@ledgerpeak.example
Address: Suite 512, 208-3375 Harwood Lane NW

Twitter: @LedgerPeakYYC
Instagram: ledgerpeakyyc

Colors
92b5d7
3276b5
33a6d7
85acd3
85cae6
0592cd

Requirements
Must have
• Some colors that match with the logo and the pictures I put in below.
• Ideally the finished product would look something like the attachments showing the color gradient I want.
Nice to have
• Please see some of the attachments I've included. This is very close to the final product that I would like to see. If someone could recreate something like those I would definitely feel pretty good about it.
• For the instagram and twitter please use the symbols/icon to represent it on the card.
Should not have
• No crazy colors and unprofessional styles. I just want clear info. Don't go outside the boundaries of the colors in the attachment and we should be good. No crazy weird fonts either.

```html
<!DOCTYPE html>
<html lang="en">
<head>
<meta charset="utf-8">
<title>Ledgerpeak Business Card</title>
<link rel="stylesheet" href="https://fonts.googleapis.com/css2?family=Cinzel:wght@400&family=Open+Sans:wght@400;700&display=swap">
<style>
  :root {
    --stage: #161617;
    --card-top: #2b2b2e;
    --card-bottom: #1c1c1e;
    --brand-blue: #1f63b3;
    --rule: #4a4a4e;
    --text-light: #e6e6e8;
    --text-soft: #c9c9cc;
  }
  * { margin: 0; padding: 0; box-sizing: border-box; }
  html, body {
    width: 1200px; height: 900px; overflow: hidden;
    background: var(--stage);
  }
  .stage {
    width: 1200px; height: 900px;
    display: flex; flex-direction: column;
    align-items: center; justify-content: center; gap: 44px;
  }
  .card {
    position: relative;
    width: 660px; height: 380px;
    border-radius: 24px;
    background: linear-gradient(160deg, var(--card-top), var(--card-bottom));
    box-shadow: 0 12px 30px rgba(0,0,0,0.55);
    font-family: "Open Sans", Arial, sans-serif;
    color: var(--text-light);
  }
  .brand {
    position: absolute;
    display: flex; align-items: center; gap: 14px;
    font-family: "Cinzel", Georgia, serif;
    font-weight: 400;
    font-size: 46px;
    letter-spacing: 1px;
    color: var(--brand-blue);
  }
  .brand-mark {
    width: 22px; height: 22px;
    background: var(--brand-blue);
  }
  .rule {
    position: absolute; height: 1px; background: var(--rule);
  }

  /* back side */
  .card-back .brand { left: 250px; top: 120px; }
  .card-back .rule { left: 220px; right: 60px; top: 212px; }
  .social-line {
    position: absolute; left: 220px; top: 300px;
    font-size: 15px; color: var(--text-light);
  }
  .social-line strong { font-weight: 700; }
  .social-line .divider { margin: 0 8px; }

  /* front side */
  .card-front .brand { left: 300px; top: 110px; }
  .card-front .rule { left: 40px; right: 50px; top: 200px; }
  .address {
    position: absolute; right: 56px; top: 220px;
    font-size: 18px; line-height: 1.3; text-align: left;
    color: var(--text-soft);
  }
  .person { position: absolute; left: 44px; bottom: 48px; }
  .person-name {
    font-family: "Cinzel", Georgia, serif;
    font-size: 24px; color: var(--brand-blue); letter-spacing: 1px;
    line-height: 1.1;
  }
  .person-title { font-size: 18px; color: var(--text-light); margin-bottom: 14px; }
  .contact {
    display: flex; align-items: center; gap: 8px;
    font-size: 19px; line-height: 1.3; color: var(--text-light);
  }
  .contact svg { width: 16px; height: 16px; fill: var(--brand-blue); flex: none; }
</style>
</head>
<body>
<main class="stage">
  <section class="card card-back" aria-label="Business card back">
    <div class="brand"><span class="brand-mark"></span>Ledgerpeak</div>
    <div class="rule"></div>
    <p class="social-line">
      <strong>Twitter:</strong> @LedgerPeakYYC<span class="divider">|</span><strong>Instagram:</strong> ledgerpeakyyc
    </p>
  </section>

  <section class="card card-front" aria-label="Business card front">
    <div class="brand"><span class="brand-mark"></span>Ledgerpeak</div>
    <div class="rule"></div>
    <address class="address" style="font-style:normal">
      Suite 512, 208-3375<br>Harwood Lane NW
    </address>
    <div class="person">
      <p class="person-name">Mark Dunn</p>
      <p class="person-title">CEO/Technical Director</p>
      <p class="contact">
        <svg viewBox="0 0 16 16" aria-hidden="true"><path d="M3 2h3l1 3-2 1.2a8 8 0 0 0 4.8 4.8L11 9l3 1v3a1 1 0 0 1-1 1A11 11 0 0 1 2 3a1 1 0 0 1 1-1z"/></svg>
        (587)430-9158
      </p>
      <p class="contact">
        <svg viewBox="0 0 16 16" aria-hidden="true"><path d="M1 3h14v10H1z M2 4.2v.3l6 4 6-4v-.3z" fill-rule="evenodd"/></svg>
        mdunn@ledgerpeak.example
      </p>
    </div>
  </section>
</main>
</body>
</html>
```